Business Card Designs

Looking to design a 3.5" x 2" standard business card for our employees.
The design needs to be sleek, simple, and modern. We would like our logo (attached) to be incorporated, but not in that colour, rather an outline of the logo in either gold or silver (whichever looks better).

Modern and Simple is what we are looking for, but be creative in incorporating the logo.

```html
<!DOCTYPE html>
<html lang="en">
<head>
<meta charset="utf-8">
<title>Harbourline Suites – Business Card</title>
<link href="https://fonts.googleapis.com/css2?family=Roboto:wght@400;500&display=swap" rel="stylesheet">
<style>
  :root {
    --backdrop: #2c2b38;
    --card-base: #161616;
    --band-top: #1d1d1d;
    --band-core: #0f0f0f;
    --band-low: #1a1a1a;
    --icon-cell: #2a2a2a;
    --text-cell: #1e1e1e;
    --text-cell-deep: #050505;
    --silver: #c9c9c9;
    --icon-grey: #8a8a8a;
    --ink: #f2f2f2;
  }
  * { margin: 0; padding: 0; box-sizing: border-box; }
  html, body {
    width: 1200px; height: 802px; overflow: hidden;
    background: var(--backdrop);
    font-family: "Roboto", Arial, sans-serif;
  }
  .stage {
    width: 1200px; height: 802px;
    display: flex; justify-content: center; align-items: center; gap: 90px;
  }
  .card {
    width: 330px; height: 578px;
    background: var(--card-base);
    display: flex; flex-direction: column;
    overflow: hidden;
  }
  /* Front */
  .front__band--top { flex: 0 0 95px; background: var(--band-top); }
  .front__band--core {
    flex: 0 0 255px; background: var(--band-core);
    display: flex; align-items: center; justify-content: center;
  }
  .front__band--low { flex: 0 0 58px; background: var(--band-low); }
  .front__band--base { flex: 1; background: var(--card-base); }

  .wordmark {
    display: flex; align-items: center; gap: 10px;
    color: var(--silver); font-weight: 500;
    letter-spacing: 0.16em; text-transform: uppercase;
  }
  .wordmark__square { width: 12px; height: 12px; background: var(--silver); }
  .wordmark--large { font-size: 17px; }
  .wordmark--small { font-size: 13px; }

  /* Back */
  .back__head {
    flex: 0 0 230px; background: var(--band-top);
    display: flex; flex-direction: column; align-items: center; justify-content: center;
    gap: 34px;
  }
  .person { text-align: center; color: var(--ink); }
  .person__name { font-size: 26px; font-weight: 400; }
  .person__name b { font-weight: 500; }
  .person__role { font-size: 15px; letter-spacing: 0.08em; margin-top: 2px; }

  .contact-row { flex: 1; display: flex; }
  .contact-row__icon {
    flex: 0 0 80px; background: var(--icon-cell);
    display: flex; align-items: center; justify-content: center;
  }
  .contact-row__icon svg { width: 20px; height: 20px; }
  .contact-row__text {
    flex: 1; background: var(--text-cell);
    display: flex; flex-direction: column; justify-content: center;
    padding-left: 24px; color: var(--ink); font-size: 13.5px; line-height: 1.3;
  }
  .contact-row--web .contact-row__icon { background: var(--text-cell); }
  .contact-row--web .contact-row__text { background: var(--text-cell-deep); }
</style>
</head>
<body>
<main class="stage">
  <section class="card card--front" aria-label="Card front">
    <div class="front__band--top"></div>
    <div class="front__band--core">
      <div class="wordmark wordmark--large"><span class="wordmark__square"></span>Harbourline Suites</div>
    </div>
    <div class="front__band--low"></div>
    <div class="front__band--base"></div>
  </section>

  <section class="card card--back" aria-label="Card back">
    <header class="back__head">
      <div class="wordmark wordmark--small"><span class="wordmark__square"></span>Harbourline Suites</div>
      <div class="person">
        <p class="person__name"><b>Daniel</b> Reyes</p>
        <p class="person__role">POSITION</p>
      </div>
    </header>

    <div class="contact-row">
      <div class="contact-row__icon">
        <svg viewBox="0 0 24 24" fill="var(--icon-grey)"><path d="M6.6 10.8a15 15 0 0 0 6.6 6.6l2.2-2.2c.3-.3.7-.4 1-.2 1.1.4 2.3.6 3.6.6.6 0 1 .4 1 1V20c0 .6-.4 1-1 1A17 17 0 0 1 3 4c0-.6.4-1 1-1h3.5c.6 0 1 .4 1 1 0 1.3.2 2.5.6 3.6.1.3 0 .7-.2 1z"/></svg>
      </div>
      <div class="contact-row__text">
        <span>d:&nbsp; 555-014-1234</span>
        <span>o:&nbsp; 555-014-2102</span>
      </div>
    </div>

    <div class="contact-row">
      <div class="contact-row__icon">
        <svg viewBox="0 0 24 24" fill="none" stroke="var(--icon-grey)" stroke-width="1.8"><path d="M12 21s-6-6.2-6-11a6 6 0 0 1 12 0c0 4.8-6 11-6 11z"/><circle cx="12" cy="10" r="2.2"/></svg>
      </div>
      <div class="contact-row__text">
        <span>48 Maple Crest Ave Suite 210</span>
        <span>Toronto, ON M4T 2B7</span>
      </div>
    </div>

    <div class="contact-row">
      <div class="contact-row__icon">
        <svg viewBox="0 0 24 24" fill="none" stroke="var(--icon-grey)" stroke-width="1.8"><rect x="3" y="6" width="18" height="13"/><path d="M3 6l9 7 9-7"/></svg>
      </div>
      <div class="contact-row__text">
        <span>dreyes@harbourline</span>
        <span>suites.com</span>
      </div>
    </div>

    <div class="contact-row contact-row--web">
      <div class="contact-row__icon">
        <svg viewBox="0 0 24 24" fill="none" stroke="var(--icon-grey)" stroke-width="1.6"><circle cx="12" cy="12" r="9"/><ellipse cx="12" cy="12" rx="4" ry="9"/><path d="M3 12h18M5 7.5h14M5 16.5h14"/></svg>
      </div>
      <div class="contact-row__text">
        <span>harbourlinesuites.com</span>
      </div>
    </div>
  </section>
</main>
</body>
</html>
```